Networking Events Calendar/Diary

We need a responsive website that can act as both an online diary/calendar and a resource for community and networking events similar to mingleroundsplaza.com (we do not want a clone, but one with similar functionality). We need to be able to host adverts, have a client area for clients to add their own events to the diary. This needs to have the functionality that clients have to pay to add recurring events. Some integration would be useful so that if a clients already has their own online diary on their website then using an API possibly to also add that event into our online diary

Industry/Entity Type

Events

Coding

Coded - Design and coding required

Number of Pages Required

5+ page

Requirements
Must have
• My project must have a calendar area, space for ads, be responsive and easily viewable on mobile. A subscribers area for clients and a way to purchase premium status so that premium events are highlighted.

```html
<!DOCTYPE html>
<html lang="en">
<head>
<meta charset="utf-8">
<title>Gather Journal – Networking Events Diary</title>
<link href="https://fonts.googleapis.com/css2?family=Open+Sans:wght@400;600;700;800&display=swap" rel="stylesheet">
<style>
:root{
  --ink:#222;
  --text:#555;
  --muted:#999;
  --line:#e3e3e3;
  --panel:#eeeeee;
  --cell:#d6d6d6;
  --accent:#2d9fd9;
  --orange:#e8902a;
  --dark:#1b1b1b;
  --label:#3d3d3d;
  --promo:#565656;
  --fans:#3b5a9a;
  --followers:#2ca7e0;
  --subs:#d9332c;
  --photo-a:#8a8f99;
  --photo-b:#4c5360;
}
*{box-sizing:border-box;margin:0;padding:0}
html,body{width:1200px;height:2869px;overflow:hidden;background:#fff}
body{font-family:"Open Sans",Arial,sans-serif;color:var(--text);font-size:11px;position:relative}
.page{position:relative;width:1200px;height:2869px}
.abs{position:absolute}
a{color:inherit;text-decoration:none}
.photo{background:linear-gradient(135deg,var(--photo-a),var(--photo-b))}
.photo.warm{background:linear-gradient(135deg,#c9b79f,#6c5a48)}
.photo.cool{background:linear-gradient(135deg,#9fb4c9,#3d4c63)}
.photo.night{background:linear-gradient(135deg,#5c4a8a,#1d1933)}
.photo.light{background:linear-gradient(135deg,#e6e4df,#a9a49b)}

/* top bar */
.topbar{left:173px;top:0;width:859px;height:34px;border-bottom:1px solid var(--line);display:flex;align-items:center;justify-content:space-between;font-size:9px;font-weight:600;color:var(--ink);text-transform:uppercase}
.topbar nav span{margin-right:14px}
.icons{display:flex;gap:8px}
.icons i{display:block;width:10px;height:10px;background:var(--ink)}
.brand{left:180px;top:50px;font-size:27px;font-weight:800;color:var(--ink);letter-spacing:.5px}

/* main nav */
.mainnav{left:173px;top:118px;width:859px;height:38px;background:var(--dark);border-top:4px solid var(--accent);display:flex;align-items:center;font-size:9.5px;font-weight:700;color:#fff;text-transform:uppercase;white-space:nowrap}
.mainnav a{padding:0 11px;height:100%;display:flex;align-items:center}
.mainnav a.current{background:#fff;color:var(--ink)}
.mainnav .search{margin-left:auto;padding:0 12px}
.ticker{left:173px;top:163px;width:859px;height:22px;display:flex;align-items:center;font-size:10px;border-bottom:1px solid var(--line)}
.ticker b{background:var(--accent);color:#fff;font-weight:600;padding:3px 8px;margin-right:12px;font-size:9px}

/* hero */
.hero-main{left:173px;top:192px;width:427px;height:271px}
.hero-tile{display:flex;align-items:flex-end;padding:10px}
.hero-caption{position:absolute;left:0;bottom:0;width:100%;background:rgba(45,159,217,.85);color:#fff;font-size:19px;font-weight:700;padding:8px 22px;text-transform:uppercase}
.btn-blue{background:var(--accent);color:#fff;font-size:10px;padding:5px 9px;font-weight:600}
.premium-tile{left:813px;top:192px;width:219px;height:126px;background:#3f3f3f;color:#fff;display:flex;flex-direction:column;align-items:center;justify-content:center;gap:10px;font-weight:700;font-size:13px;text-transform:uppercase;text-align:center}

/* section heads */
.head{height:20px;border-bottom:1px solid var(--line);display:flex;justify-content:space-between;align-items:flex-start}
.head b{background:var(--label);color:#fff;font-size:9.5px;font-weight:600;padding:3px 9px}
.head small{font-size:9px;color:var(--muted);border:1px solid var(--line);padding:1px 6px}
.pager{display:flex;gap:3px}
.pager i{width:14px;height:14px;border:1px solid #ccc;display:flex;align-items:center;justify-content:center;font-style:normal;font-size:9px;color:#666}

/* events */
.event{width:550px;height:120px;background:var(--panel);display:flex;align-items:center}
.event .date{width:100px;text-align:center;color:var(--ink);border-right:1px solid #ccc;height:80px;display:flex;flex-direction:column;justify-content:center}
.event .date strong{font-size:22px;font-weight:400;text-transform:uppercase}
.event .date span{font-size:14px;margin-top:10px}
.event .body{width:330px;padding:0 14px;position:relative;height:96px;border-right:1px solid #ccc}
.event h3{color:var(--orange);font-size:13px;font-weight:600;text-transform:uppercase;margin-bottom:6px}
.event p{font-size:10px;line-height:1.45}
.event .share{position:absolute;right:10px;bottom:0;display:flex;gap:4px}
.event .share i{width:9px;height:9px;background:#666}
.event .premium{flex:1;display:flex;flex-direction:column;align-items:center;color:var(--accent);font-size:11px;text-transform:uppercase;text-align:center;line-height:1.35}

/* blog */
.post-title{color:var(--accent);font-size:15px;font-weight:700;line-height:1.35}
.meta{font-size:10px;color:var(--muted)}
.meta em{font-style:normal;color:var(--accent)}
.excerpt{font-size:10.5px;line-height:1.5}
.mini{display:flex;gap:10px;width:277px;height:72px}
.mini .thumb{width:97px;height:70px;flex:none}
.mini h4{color:var(--accent);font-size:11.5px;font-weight:600;line-height:1.3;margin-bottom:4px}
.mini .meta{color:var(--ink)}

/* tips */
.tip{width:257px;height:170px}
.tip span{position:absolute;left:0;bottom:0;width:100%;padding:10px 12px;color:#fff;font-size:14px;font-weight:700;line-height:1.3;background:linear-gradient(transparent,rgba(0,0,0,.75))}

/* news */
.news{width:550px;background:var(--panel);padding:16px 20px;overflow:hidden}
.news h3{color:var(--accent);font-size:13px;font-weight:600;margin-bottom:12px}
.news p{font-size:10px;line-height:1.6;color:#888}

/* sidebar */
.ad{width:271px;background:#8e8e8e;border:1px solid #777}
.ad svg{display:block}
.countdown{display:grid;grid-template-columns:repeat(4,1fr);border:1px solid var(--line)}
.countdown div{text-align:center;border-right:1px solid var(--line)}
.countdown b{display:block;font-size:13px;font-weight:400;color:var(--ink);padding:5px 0;border-bottom:1px solid var(--line)}
.countdown small{font-size:8px;text-transform:uppercase}
.btn-orange{background:var(--orange);color:#fff;font-size:9px;font-weight:700;padding:4px 8px;text-transform:uppercase}
.cal-bar{width:251px;height:32px;background:var(--label);color:#fff;display:flex;justify-content:space-between;align-items:center;padding:0 10px;font-weight:700;font-size:13px}
.cal-grid{display:grid;grid-template-columns:repeat(7,31px);gap:5px}
.cal-grid span{height:31px;background:var(--cell);display:flex;align-items:center;justify-content:center;font-size:11px;color:var(--ink)}
.cal-grid .dow{background:none;font-weight:700;height:22px}
.cal-grid .blank{background:#e9e9e9}
.cal-grid .today{background:var(--orange);color:#fff;font-weight:700}
.promo{width:271px;height:180px;background:var(--promo);color:#fff;padding:16px}
.promo h3{font-size:16px;font-weight:400;line-height:1.3;margin-bottom:12px}
.promo p{font-size:9.5px;line-height:1.5;color:#ddd;margin-bottom:14px}
.promo a{font-weight:700;font-size:10px}
.social{width:271px;height:24px;display:flex;align-items:center;color:#fff;font-size:9px;padding:0 0 0 6px;margin-bottom:6px}
.social i{width:10px;height:10px;background:#fff;margin-right:10px}
.social b{width:50px}
.social em{margin-left:auto;font-style:normal;font-weight:700;padding:0 10px;background:rgba(0,0,0,.15);height:100%;display:flex;align-items:center}

.widget{width:271px;height:516px;border:1px solid var(--line);background:#fff;overflow:hidden}
.widget .cover{height:110px;position:relative}
.widget .cover b{position:absolute;left:10px;top:8px;background:#fff;color:var(--ink);font-size:10px;padding:4px 6px}
.widget .follow{padding:8px 10px;font-size:9px;color:#777}
.widget .faces{display:flex;gap:3px;margin-top:5px}
.widget .faces i{width:18px;height:18px;background:#c7c7c7}
.widget .post{margin:6px 10px;border:1px solid var(--line);padding:8px;font-size:9px;line-height:1.5}
.widget .post b{color:var(--ink);font-size:10px}

/* footer */
.footer{left:173px;top:2443px;width:859px;height:389px;background:var(--dark);color:#ccc}
.footer .fbrand{left:20px;top:45px;font-size:22px;font-weight:800;color:#fff}
.footer .about{left:20px;top:120px;width:220px;font-size:10.5px;line-height:1.5}
.footer .contact{left:20px;top:230px;font-size:10.5px}
.footer .contact a{color:var(--accent)}
.footer .circles{left:40px;top:268px;display:flex;gap:14px}
.footer .circles i{width:11px;height:11px;border-radius:50%;background:#fff}
.footer .tag{left:307px;top:34px;background:#fff;color:var(--ink);font-size:10px;padding:3px 10px}
.links{width:257px;font-size:10.5px;color:#ddd}
.links li{list-style:none;height:35px;display:flex;align-items:center;border-bottom:1px solid #333}
.copyright{left:173px;top:2840px;width:859px;height:29px;display:flex;justify-content:space-between;align-items:center;font-size:9.5px;color:var(--ink)}
.copyright nav span{margin-left:26px}
</style>
</head>
<body>
<div class="page">

  <header>
    <div class="abs topbar">
      <nav><span>Friday, December 18, 2015</span><span>Sign in / Join</span><span>Advertise ▾</span><span>Contact</span></nav>
      <div class="icons"><i></i><i></i><i></i><i></i><i></i></div>
    </div>
    <div class="abs brand">GATHER JOURNAL</div>
    <nav class="abs mainnav">
      <a class="current">Home</a><a>Events by Region</a><a>Events by Town / City</a><a>Events for Women</a><a>Workshop / Seminars</a><a>Business Shows</a><a>Blog</a><a>Event Franchises</a>
      <a class="search"><svg width="11" height="11" viewBox="0 0 12 12"><circle cx="5" cy="5" r="3.8" fill="none" stroke="#fff" stroke-width="1.6"/><line x1="7.8" y1="7.8" x2="11" y2="11" stroke="#fff" stroke-width="1.8"/></svg></a>
    </nav>
    <div class="abs ticker"><b>Recent Events</b>Sed ut perspiciatis unde omnis iste natus error sit voluptatem</div>
  </header>

  <section class="hero">
    <div class="abs hero-main photo warm" role="img" aria-label="Group of business people raising glasses at a networking event">
      <div class="hero-caption">Welcome to Gather Journal</div>
    </div>
    <div class="abs hero-tile photo cool" style="left:607px;top:192px;width:199px;height:133px" role="img" aria-label="Business people shaking hands at a meeting">
      <span class="btn-blue">Subscribe to our Event Bulletin »</span>
    </div>
    <div class="abs hero-tile photo" style="left:607px;top:330px;width:199px;height:133px" role="img" aria-label="Colleagues chatting at a networking reception">
      <span class="btn-blue">View Networking Tips »</span>
    </div>
    <div class="abs premium-tile">
      <svg width="40" height="40" viewBox="0 0 40 40"><circle cx="20" cy="20" r="18" fill="none" stroke="#fff" stroke-width="2"/><circle cx="20" cy="17" r="6" fill="#fff"/><path d="M15 22 L13 31 L20 28 L27 31 L25 22" fill="#fff"/></svg>
      Purchase Premium<br>Status
    </div>
    <div class="abs hero-tile photo light" style="left:813px;top:325px;width:219px;height:138px" role="img" aria-label="Business people at a conference table">
      <span class="btn-blue">Register to Add Event »</span>
    </div>
  </section>

  <main>
    <section class="abs" style="left:190px;top:473px;width:550px">
      <div class="head"><b>Upcoming Events</b><small>All ▾</small></div>
      <article class="event" style="margin-top:18px">
        <div class="date"><strong>28 Dec</strong><span>05.30pm</span></div>
        <div class="body"><h3>Quia non numquam eius modi</h3><p>Dolore magnam aliquam quaerat voluptatem. Ut enim ad minima veniam, quis nostrum exercitation em ullam corporis suscipit laboriosam.</p><div class="share"><i></i><i></i><i></i></div></div>
        <div class="premium"><svg width="30" height="30" viewBox="0 0 30 30"><circle cx="15" cy="12" r="7" fill="none" stroke="#2d9fd9" stroke-width="2"/><path d="M10 18 L8 27 L15 24 L22 27 L20 18" fill="none" stroke="#2d9fd9" stroke-width="2"/></svg>Premium<br>Profile</div>
      </article>
      <article class="event" style="margin-top:12px">
        <div class="date"><strong>8 Jan</strong><span>11.00am</span></div>
        <div class="body"><h3>Nisi ut aliquid ex ea commodi</h3><p>Ullam corporis suscipit laboriosam, nisi ut aliquid ex ea commodi consequatur quis autem vel eum iure reprehenderit qui in ea voluptate velit esse quam.</p><div class="share"><i></i><i></i><i></i></div></div>
        <div class="premium"><svg width="30" height="30" viewBox="0 0 30 30"><circle cx="15" cy="12" r="7" fill="none" stroke="#2d9fd9" stroke-width="2"/><path d="M10 18 L8 27 L15 24 L22 27 L20 18" fill="none" stroke="#2d9fd9" stroke-width="2"/></svg>Premium<br>Profile</div>
      </article>
      <article class="event" style="margin-top:12px">
        <div class="date"><strong>24 Jan</strong><span>02.30pm</span></div>
        <div class="body"><h3>Et harum quidem rerum facilis</h3><p>Et aut officiis debitis aut rerum necessitatibus saepe et ut et voluptates repudiandae sint et molestiae non recusandae. Itaque earum rerum hic tenetur a sapiente delectus.</p><div class="share"><i></i><i></i><i></i></div></div>
        <div class="premium"><svg width="30" height="30" viewBox="0 0 30 30"><circle cx="15" cy="12" r="7" fill="none" stroke="#2d9fd9" stroke-width="2"/><path d="M10 18 L8 27 L15 24 L22 27 L20 18" fill="none" stroke="#2d9fd9" stroke-width="2"/></svg>Premium<br>Profile</div>
      </article>
      <div class="pager" style="margin-top:16px"><i>‹</i><i>›</i></div>
    </section>

    <section class="abs" style="left:190px;top:955px;width:550px;height:420px">
      <div class="head"><b>Latest Blog Posts</b><small>All ▾</small></div>
      <div class="abs photo light" style="left:0;top:35px;width:254px;height:170px" role="img" aria-label="Elegant dinner table set for an event"></div>
      <div class="abs" style="left:0;top:215px;width:254px">
        <h3 class="post-title">Et harum quidem rerum facilis est et expedita distinctio</h3>
        <div class="meta" style="margin-top:8px"><em>John Doe</em> - Dec 12, 2015</div>
        <p class="excerpt" style="margin-top:8px">Nam libero tempore, cum soluta nobis est eligendi optio cumque nihil impedit quo minus id quod maxime placeat [...]</p>
      </div>
      <div class="abs" style="left:273px;top:35px">
        <div class="mini"><div class="thumb photo night" role="img" aria-label="Crowd at an evening event"></div><div><h4>Temporibus autem quibu sd am et aut officiisodu</h4><div class="meta">John Doe - Dec 12, 2015</div></div></div>
        <div class="mini" style="margin-top:12px"><div class="thumb photo warm" role="img" aria-label="Banquet hall with round tables"></div><div><h4>Repudiandae sint et mol estiae non</h4><div class="meta">Lora Leo - Dec 10, 2015</div></div></div>
        <div class="mini" style="margin-top:12px"><div class="thumb photo night" role="img" aria-label="Conference stage with audience"></div><div><h4>Minis dolor repellendus. Temporibus autem</h4><div class="meta">Ray Matrin - Dec 08, 2015</div></div></div>
        <div class="mini" style="margin-top:12px"><div class="thumb photo cool" role="img" aria-label="Audience seated at a seminar"></div><div><h4>Sed ut perspiciatis unde omnis iste</h4><div class="meta">Seda Quiam - Dec 02, 2015</div></div></div>
      </div>
      <div class="abs pager" style="left:0;top:402px"><i>‹</i><i>›</i></div>
    </section>

    <section class="abs" style="left:190px;top:1411px;width:550px;height:400px">
      <div class="head"><b>Networking Tips</b><small>All ▾</small></div>
      <div class="abs tip photo light" style="left:0;top:35px" role="img" aria-label="Speaker presenting to a room"><span>Nisi ut aliquid ex ea commodi conseq uatur quis autem</span></div>
      <div class="abs tip photo warm" style="left:273px;top:35px" role="img" aria-label="Glasses raised in a toast"><span>Et illum qui dolorem eum fugiat quo voluptas nulla pariatur</span></div>
      <div class="abs tip photo cool" style="left:0;top:224px" role="img" aria-label="People talking at a business mixer"><span>Veritatis et quasi architecto beatae vitae dicta</span></div>
      <div class="abs tip photo" style="left:273px;top:224px" role="img" aria-label="Professionals networking in a lobby"><span>Placeat facere possimus, omnis voluptas assumenda</span></div>
    </section>

    <section class="abs" style="left:190px;top:1872px;width:550px">
      <div class="head"><b>Networking News</b><small>All ▾</small></div>
      <article class="news" style="margin-top:14px;height:150px">
        <h3>» Vero eos et accusamus et iusto odio dignissimos ducimus qui blanditiis</h3>
        <p>Raesentium voluptatum deleniti atque corrupti quos dolores et quas molestias excepturi sint occaecati cupiditate non provident, similique sunt in culpa qui officia deserunt mollitia animi, id est laborum et dolorum fuga. Et harum quidem rerum facilis est et expedita distinctio. Nam libero tempore, cum soluta nobis est eligendi optio cumque nihil impedit quo minus id quod maxime placeat facere possimus, omnis voluptas assumenda est, omnis dolor repellendus.</p>
      </article>
      <article class="news" style="margin-top:14px;height:112px">
        <h3>» Qui officia deserunt mollitia animi, id est laborum et dolorum fuga</h3>
        <p>Temporibus autem quibusdam et aut officiis debitis aut rerum necessitatibus saepe eveniet ut et voluptates repudiandae sint et molestiae non recusandae. Itaque earum rerum hic tenetur a sapiente delectus, ut aut reiciendis voluptatibus maiores alias consequatur aut perferendis.</p>
      </article>
      <article class="news" style="margin-top:14px;height:112px">
        <h3>» Omnis dolor repellendus temporibus autem quibusdam et aut</h3>
        <p>Et illum qui dolorem eum fugiat quo voluptas nulla pariatur. Nam libero tempore, cum soluta nobis est eligendi optio cumque nihil impedit quo minus id quod maxime placeat facere possimus, omnis voluptas assumenda est, omnis dolor repellendus.</p>
      </article>
      <div class="pager" style="margin-top:12px"><i>‹</i><i>›</i></div>
    </section>
  </main>

  <aside>
    <div class="abs ad" style="left:756px;top:473px;height:216px">
      <svg width="269" height="214" viewBox="0 0 269 214"><line x1="0" y1="0" x2="269" y2="214" stroke="#6f6f6f"/><line x1="269" y1="0" x2="0" y2="214" stroke="#6f6f6f"/><rect x="104" y="96" width="61" height="20" fill="#8e8e8e"/><text x="134.5" y="110" text-anchor="middle" font-family="Open Sans, sans-serif" font-size="11" fill="#333">Ad Space</text></svg>
    </div>

    <div class="abs" style="left:756px;top:713px;width:271px">
      <div class="head"><b>Next Event Countdown</b></div>
      <div style="display:flex;gap:6px;margin-top:22px">
        <div class="photo night" style="width:76px;height:76px" role="img" aria-label="Evening event crowd"></div>
        <div style="flex:1">
          <div class="countdown"><div><b>43</b><small>Days</small></div><div><b>15</b><small>Hours</small></div><div><b>45</b><small>Min</small></div><div style="border-right:0"><b>10</b><small>Sec</small></div></div>
          <div style="display:flex;align-items:center;gap:6px;margin-top:10px;font-size:9.5px;color:var(--ink)"><span class="btn-orange">More Info</span>⏱ 12:30pm-04:30pm</div>
        </div>
      </div>
    </div>

    <div class="abs" style="left:756px;top:874px;width:271px">
      <div class="head"><b>View Calendar Schedule</b></div>
      <div style="padding:0 10px;margin-top:20px">
        <div class="cal-bar"><span>◀</span>December 2015<span>▶</span></div>
        <div class="cal-grid" style="margin-top:6px">
          <span class="dow">Su</span><span class="dow">Mo</span><span class="dow">Tu</span><span class="dow">We</span><span class="dow">Th</span><span class="dow">Fr</span><span class="dow">Sa</span>
          <span class="blank"></span><span class="blank"></span><span>1</span><span>2</span><span>3</span><span>4</span><span>5</span>
          <span>6</span><span>7</span><span>8</span><span>9</span><span>10</span><span>11</span><span>12</span>
          <span>13</span><span>14</span><span>15</span><span>16</span><span>17</span><span>18</span><span>19</span>
          <span>20</span><span>21</span><span>22</span><span>23</span><span>24</span><span class="today">25</span><span>26</span>
          <span>27</span><span>28</span><span>29</span><span>30</span><span>31</span><span class="blank"></span><span class="blank"></span>
        </div>
      </div>
    </div>

    <div class="abs promo" style="left:756px;top:1277px">
      <h3>Event Organisers - Upgrade to Premium Profile for only £4.99/month!</h3>
      <p>Sed ut perspiciatis unde omnis iste natus error sit voluptatem accusantium dolor emque laudantium, totam rem aperiam, eaque ipsa quae ab illo inventore veritatis et quasi.</p>
      <a>FIND MORE ❯</a>
    </div>

    <div class="abs" style="left:756px;top:1495px;width:271px">
      <div class="head"><b>Stay Connected</b></div>
      <div style="margin-top:16px">
        <div class="social" style="background:var(--fans)"><i></i><b>165,957</b>Fans<em>LIKE</em></div>
        <div class="social" style="background:var(--followers)"><i></i><b>56,450</b>Followers<em>FOLLOW</em></div>
        <div class="social" style="background:var(--subs)"><i></i><b>5,254</b>Subscriber<em>SUBSCRIBE</em></div>
      </div>
    </div>

    <div class="abs ad" style="left:756px;top:1661px;height:223px">
      <svg width="269" height="221" viewBox="0 0 269 221"><line x1="0" y1="0" x2="269" y2="221" stroke="#6f6f6f"/><line x1="269" y1="0" x2="0" y2="221" stroke="#6f6f6f"/><rect x="104" y="100" width="61" height="20" fill="#8e8e8e"/><text x="134.5" y="114" text-anchor="middle" font-family="Open Sans, sans-serif" font-size="11" fill="#333">Ad Space</text></svg>
    </div>

    <div class="abs widget" style="left:756px;top:1913px">
      <div class="cover photo cool" role="img" aria-label="Page cover showing a business meeting"><b>Gather Journal</b></div>
      <div class="follow">Be the first of your friends to like this
        <div class="faces"><i></i><i></i><i></i><i></i><i></i><i></i><i></i><i></i></div>
      </div>
      <div class="post">
        <b>Gather Journal</b><br>
        Great turnout at last night's mixer in the city. Thank you to everyone who came along, shared ideas and made new contacts. Our next session is open for booking now, so check the diary and save your seat early.
        <div class="photo warm" style="height:110px;margin-top:8px" role="img" aria-label="Guests mingling at a networking evening"></div>
        <div style="margin-top:6px;color:#888">12,174 Views</div>
        <div style="display:flex;gap:30px;margin-top:8px;color:#666">💬 Comment <span>↗ Share</span></div>
      </div>
    </div>
  </aside>

  <footer class="abs footer">
    <div class="abs fbrand">GATHER JOURNAL</div>
    <p class="abs about">Quis nostrum exercitationem ullam corporis su suscipit laboriosam, nisi ut aliquid ex ea commodi consequatur. Quis autem vel eum iure reprehenderit qui in ea voluptate velit esse quam nihil molestiae.</p>
    <div class="abs contact">Contact us: <a>info@gatherjournal.com</a></div>
    <div class="abs circles"><i></i><i></i><i></i><i></i><i></i></div>
    <div class="abs tag">More About Gather Journal</div>
    <ul class="abs links" style="left:307px;top:68px">
      <li>Log in</li><li>Contact us</li><li>Subscribe to our Weekly Bulletin</li><li>Register to Add Events</li><li>Testimonials</li><li>Online Marketing Mentoring Sessions</li><li style="height:44px;line-height:1.35">Download 'A Quick Guide to Business Networking'</li>
    </ul>
    <ul class="abs links" style="left:582px;top:68px">
      <li>Networking Events by Region</li><li>Networking Events by Town/City</li><li>Networking Events for Women</li><li>Workshops/Seminars</li><li>Business Shows</li><li>Blog</li><li>Networking News</li>
    </ul>
  </footer>

  <div class="abs copyright">
    <span>© Copyright 2015 - Gather Journal</span>
    <nav><span>Disclaimer</span><span>Privacy</span><span>Advertisement</span><span>Contact Us</span></nav>
  </div>

</div>
</body>
</html>
```